Structural Engineering Business Card

Veltrow Drafts does residential house plans for clients in Central Florida. Would like simple but elegant business card that is appropriate for a house plan engineering company. Prefer black business card with black/white them but open to other shades of blue. I uploaded a sample card that I came across that looked good but please come up with your own creative designs.

Contact Information for Business Card

Name, Title, Phone, Email, Address, website

```html
<!DOCTYPE html>
<html lang="en">
<head>
<meta charset="utf-8">
<title>Veltrow Drafts — Business Card</title>
<link rel="stylesheet" href="https://fonts.googleapis.com/css2?family=Open+Sans:wght@400;600;800&display=swap">
<style>
  :root {
    --page: #d9d6d1;
    --card: #020202;
    --ink: #ffffff;
    --accent: #5bb8df;
    --drawing-hi: #2a2a2a;
    --drawing-lo: #0a0a0a;
    --rule: #bfbfbf;
  }
  * { box-sizing: border-box; margin: 0; padding: 0; }
  html, body { width: 1200px; height: 900px; overflow: hidden; }
  body {
    background: var(--page);
    font-family: "Open Sans", Arial, sans-serif;
    color: var(--ink);
    position: relative;
  }
  .card {
    position: absolute;
    left: 250px;
    width: 700px;
    height: 400px;
    background: var(--card);
    overflow: hidden;
    box-shadow: 0 8px 24px rgba(0,0,0,.25);
  }
  .card--front { top: 35px; }
  .card--back { top: 465px; }

  .drawing-area {
    position: absolute;
    background: radial-gradient(ellipse at 45% 45%, var(--drawing-hi), var(--drawing-lo) 75%);
    opacity: .9;
  }
  .card--front .drawing-area { left: 0; top: 0; width: 440px; height: 330px; }
  .card--back .drawing-area { right: 0; top: 0; width: 430px; height: 240px; }

  .wordmark {
    position: absolute;
    font-weight: 800;
    color: var(--ink);
    letter-spacing: 1px;
    white-space: nowrap;
    line-height: 1;
  }
  .card--front .wordmark { right: 40px; top: 190px; font-size: 50px; }
  .card--back .wordmark { left: 44px; top: 318px; font-size: 44px; }

  .identity { position: absolute; left: 44px; top: 60px; }
  .identity__name {
    font-weight: 800;
    color: var(--accent);
    font-size: 24px;
    letter-spacing: .5px;
  }
  .identity__title { font-size: 20px; font-weight: 400; margin-top: 2px; }

  .contact-list {
    position: absolute;
    left: 60px;
    top: 170px;
    list-style: none;
    font-size: 21px;
  }
  .contact-list li { display: flex; align-items: center; gap: 12px; height: 34px; }
  .contact-list svg { width: 18px; height: 18px; fill: var(--accent); flex: none; }

  .divider {
    position: absolute;
    left: 44px;
    top: 300px;
    width: 420px;
    height: 1px;
    background: var(--rule);
  }

  .address {
    position: absolute;
    right: 40px;
    top: 250px;
    text-align: right;
    font-size: 20px;
    line-height: 1.3;
  }
</style>
</head>
<body>

<section class="card card--front" aria-label="Card front">
  <div class="drawing-area" role="img" aria-label="Faint architectural elevation drawing of a house in grey linework"></div>
  <div class="wordmark">VELTROW DRAFTS</div>
</section>

<section class="card card--back" aria-label="Card back">
  <div class="drawing-area" role="img" aria-label="Faint architectural elevation drawing of a house in grey linework"></div>

  <div class="identity">
    <p class="identity__name">MARCUS HALE</p>
    <p class="identity__title">Architectural Director</p>
  </div>

  <ul class="contact-list">
    <li>
      <svg viewBox="0 0 24 24" aria-hidden="true"><path d="M6.6 10.8a15.1 15.1 0 0 0 6.6 6.6l2.2-2.2a1 1 0 0 1 1-.25 11.4 11.4 0 0 0 3.6.57 1 1 0 0 1 1 1V20a1 1 0 0 1-1 1A17 17 0 0 1 3 4a1 1 0 0 1 1-1h3.5a1 1 0 0 1 1 1c0 1.25.2 2.45.57 3.6a1 1 0 0 1-.25 1z"/></svg>
      555-014-2273
    </li>
    <li>
      <svg viewBox="0 0 24 24" aria-hidden="true"><path d="M3 5h18a1 1 0 0 1 1 1v12a1 1 0 0 1-1 1H3a1 1 0 0 1-1-1V6a1 1 0 0 1 1-1zm9 7.5L20 7H4z"/></svg>
      info@veltrowdrafts.com
    </li>
    <li>
      <svg viewBox="0 0 24 24" aria-hidden="true"><path d="M12 2a10 10 0 1 0 0 20 10 10 0 0 0 0-20zm0 2a8 8 0 0 1 7.75 6H15.9A14 14 0 0 0 13.7 4.2 8 8 0 0 1 12 4zm-2 .3A12 12 0 0 0 8.1 10H4.25A8 8 0 0 1 10 4.3zM4.25 14H8.1a12 12 0 0 0 1.9 5.7A8 8 0 0 1 4.25 14zM12 20a10 10 0 0 1-1.9-6h3.8A10 10 0 0 1 12 20zm-1.9-10A10 10 0 0 1 12 4.2 10 10 0 0 1 13.9 10zm3.6 9.8a14 14 0 0 0 2.2-5.8h3.85a8 8 0 0 1-6.05 5.8z"/></svg>
      www.veltrowdrafts.com
    </li>
  </ul>

  <div class="divider"></div>

  <p class="address">42 Oakridge Lane<br>Orlando 32801</p>

  <div class="wordmark">VELTROW DRAFTS</div>
</section>

</body>
</html>
```